Need Business Card Design, Letterhead and a Basic Form layout based on Existing Logo

We need (1) a business card design, (2) a letterhead design and (3) a basic form layout for an international holding company. This holding company has just formed two (2) sub-companies. The logo is the same for each company with only a simple word change for each company. The business card, letterhead and form design will be essentially the same for each company... with only the one word change being different.
The names of the companies are as follows:
1. Ridgeway Trust Services
2. Ridgeway Immigration Services
The design for the business card, letterhead and Form must be strong, clean and classy.
Our clients will be older, wealthy and mostly Asian. The design must project strength, stability and confidence.
The card may contain the following data:
1. The Logo
2. The name of the person
3. The title of the person
4. The address of the company
5. The Company Phone number
6. The personal mobile number
7. The Skype number (VOIP)
8. The WICKR number (IM)
9. The email
10. The website
We will attach AI files of our logo for the "Ridgeway Trust Services" company in the colors Black/White and Blue in both Horizontal and Vertical format... We have also included separate files of the logo icon.
We uploaded the AI files to give the designer the maximum options regarding color and effects. We included the separate files for the icon because we would like to give the designer the option of a watermark. Also, we think it might be nice to highlight the icon on the back of the card perhaps with the website address.
We are not sure which colors or color combinations would be best for these two companies. We know the colors must again project strength, stability and confidence. Perhaps, a combination that might include Tan, Black and White... not sure... need design help... remember this has to have the presence of a bank-like institution... no cartoonish designs or flashy color combinations... please.
The basic form layout will be used for various questionaires, input sheets and instructions.... etc.
NOTE: The fonts used in the logo are Trajan Pro Bold for word "RIDGEWAY" and Trajan Pro Regular for "XXXXXXXXX SERVICES".

```html
<!DOCTYPE html>
<html lang="en">
<head>
<meta charset="utf-8">
<title>Ridgeway Trust Services – Business Card</title>
<link rel="stylesheet" href="https://fonts.googleapis.com/css2?family=Cinzel:wght@400&family=Open+Sans:wght@400&display=swap">
<style>
  :root {
    --backdrop: #e6e4e0;
    --card: #ffffff;
    --ink: #1a1a1a;
    --ink-soft: #444444;
    --rule-grey: #b9b9b9;
    --band-black: #111111;
    --icon-red: #c8332b;
    --icon-blue: #2f7fc8;
  }
  * { box-sizing: border-box; margin: 0; padding: 0; }
  html, body { width: 1200px; height: 720px; overflow: hidden; }
  body {
    background: var(--backdrop);
    font-family: "Open Sans", Arial, sans-serif;
    color: var(--ink);
    position: relative;
  }
  .card {
    position: absolute;
    top: 210px;
    width: 520px;
    height: 300px;
    background: var(--card);
    box-shadow: 0 2px 6px rgba(0,0,0,.12);
  }
  .card--front { left: 50px; }
  .card--back { left: 630px; }

  /* front */
  .edge-band {
    position: absolute; left: 0; top: 0; bottom: 0; width: 14px;
    background: var(--rule-grey);
  }
  .edge-band__dark {
    position: absolute; left: 0; bottom: 0; width: 14px; height: 150px;
    background: var(--band-black);
  }
  .brand {
    display: flex; align-items: center; gap: 18px;
  }
  .brand__mark {
    width: 62px; height: 62px; background: var(--ink); flex: none;
  }
  .brand__name {
    font-family: "Cinzel", "Times New Roman", serif;
    font-weight: 400;
    color: var(--ink);
    line-height: 1;
  }
  .brand__name-main { display: block; font-size: 34px; letter-spacing: 1px; }
  .brand__name-sub { display: block; font-size: 17px; margin: 4px 0 0 22px; letter-spacing: .5px; }
  .card--front .brand { position: absolute; left: 42px; top: 38px; }

  .person {
    position: absolute; right: 34px; top: 50px; text-align: right;
    font-family: "Cinzel", "Times New Roman", serif;
  }
  .person__name { font-size: 17px; letter-spacing: .5px; }
  .person__title { font-size: 11px; color: var(--ink-soft); letter-spacing: 1px; }

  .contacts {
    position: absolute; left: 38px; top: 150px; list-style: none;
    font-size: 12.5px; line-height: 18px; color: var(--ink);
  }
  .contacts li { display: flex; align-items: center; gap: 6px; }
  .contacts svg { width: 11px; height: 11px; flex: none; }
  .address {
    position: absolute; left: 38px; bottom: 18px;
    font-size: 11.5px; color: var(--ink-soft);
  }

  /* back */
  .card--back .brand {
    position: absolute; left: 0; right: 0; top: 84px;
    flex-direction: column; gap: 14px;
  }
  .card--back .brand__mark { width: 70px; height: 70px; }
  .card--back .brand__name-main { font-size: 40px; }
  .card--back .brand__name-sub { font-size: 19px; margin: 2px 0 0 60px; }
  .website {
    position: absolute; left: 0; right: 0; bottom: 40px; text-align: center;
    font-size: 15px; letter-spacing: 3px; color: var(--ink-soft);
  }
</style>
</head>
<body>
  <section class="card card--front" aria-label="Business card front">
    <div class="edge-band"><div class="edge-band__dark"></div></div>

    <div class="brand">
      <div class="brand__mark"></div>
      <div class="brand__name">
        <span class="brand__name-main">RIDGEWAY</span>
        <span class="brand__name-sub">Trust Services</span>
      </div>
    </div>

    <div class="person">
      <p class="person__name">Your Name</p>
      <p class="person__title">TITLE</p>
    </div>

    <ul class="contacts">
      <li>
        <svg viewBox="0 0 12 12" aria-hidden="true"><circle cx="6" cy="6" r="5.5" fill="none" stroke="#1a1a1a"/><path d="M4 3.2l1 1.3-.7.8c.5 1 1.2 1.7 2.2 2.2l.8-.7 1.3 1-.6 1.1C5.7 8.7 3.3 6.3 3 4z" fill="#1a1a1a"/></svg>
        012-345-6789
      </li>
      <li>
        <svg viewBox="0 0 12 12" aria-hidden="true"><rect x="3.5" y="1" width="5" height="10" rx="1" fill="#1a1a1a"/><rect x="4.3" y="2.2" width="3.4" height="6.3" fill="#fff"/></svg>
        012-345-6789
      </li>
      <li>
        <svg viewBox="0 0 12 12" aria-hidden="true"><circle cx="6" cy="6" r="5.5" fill="var(--icon-blue)"/></svg>
        012-345-6789
      </li>
      <li>
        <svg viewBox="0 0 12 12" aria-hidden="true"><rect x=".5" y=".5" width="11" height="11" fill="var(--icon-red)"/></svg>
        012-345-6789
      </li>
      <li>
        <svg viewBox="0 0 12 12" aria-hidden="true"><rect x=".5" y="2" width="11" height="8" fill="var(--icon-blue)"/><path d="M.5 2l5.5 4.5L11.5 2" fill="none" stroke="#fff"/></svg>
        inquiry@ridgewaytrust.com
      </li>
      <li>
        <svg viewBox="0 0 12 12" aria-hidden="true"><circle cx="6" cy="6" r="5" fill="none" stroke="#1a1a1a"/><ellipse cx="6" cy="6" rx="2.2" ry="5" fill="none" stroke="#1a1a1a"/><path d="M1 6h10" stroke="#1a1a1a"/></svg>
        www.ridgewaytrust.com
      </li>
    </ul>

    <p class="address">Street Name, City Name, Zip Code-00000</p>
  </section>

  <section class="card card--back" aria-label="Business card back">
    <div class="brand">
      <div class="brand__mark"></div>
      <div class="brand__name">
        <span class="brand__name-main">RIDGEWAY</span>
        <span class="brand__name-sub">Trust Services</span>
      </div>
    </div>
    <p class="website">www.ridgewaytrust.com</p>
  </section>
</body>
</html>
```